Web Design Project

We need a design for the actual web.
http://mirenda.vospel.tv/
It will be a cakes and cupcakes online shop.

It is a one page site, with five anchors.

Inicio (Home)
Here it will show a brief explanation about our shop, just explaining we sell really nice cakes and cupcakes. Also we want to show a slide gallery, like the one it is working, but with not nice choosen pictures.

Productos/Tortas
This two anchors will be just one at the end, but I wanted to show the two options for accessing the different products, tabs or buttons. You can click on the firsts images on that links for see the "pop up image" with a better explanation of every product.

Contacto
Here it will show a little form, that will only appear in smartphones and maybe tablets, this form needs to be similar and much more simple than the principal form (the next anchor), so just focus on it once the next one its done.

Form
This will be the way the users will send the orders, its a complex form, focused on the UX. We dont want the user to type too much and we want it to surprise the user and fell really comfortable.

Requirements
Must have

• -Must have side menu, but you can redesign it completelly, but with the same structure
-Its important to focus all the content in the top and middle, we arent sure about users screens and it we set info at the footer, maybe its not gonna show (no scroll vertical).
-You can change all the colours of the site, we are open to new visions, you can surprise us.

```html
<!DOCTYPE html>
<html lang="es">
<head>
<meta charset="utf-8">
<title>Hazel Bakes – Pastelería casera</title>
<link rel="stylesheet" href="https://fonts.googleapis.com/css2?family=Dancing+Script:wght@500;700&family=Arimo:wght@400;700&display=swap">
<style>
  :root {
    --cream: #fdf6c6;
    --teal: #3a9fad;
    --teal-light: #5cbcc9;
    --teal-dark: #217c8a;
    --ink: #2f2f2f;
    --heading: #3aa3b4;
    --gold: #fbd320;
    --gold-dark: #f2b500;
    --white: #ffffff;
    --panel-top: #f6f6f6;
    --script: "Dancing Script", cursive;
    --sans: "Arimo", Arial, sans-serif;
  }
  * { box-sizing: border-box; margin: 0; padding: 0; }
  html, body { width: 1200px; height: 738px; overflow: hidden; }
  body { background: var(--cream); font-family: var(--sans); color: var(--ink); position: relative; }

  .content-panel {
    position: absolute; left: 156px; top: 156px; width: 886px; height: 600px;
    background: linear-gradient(to bottom, var(--panel-top) 0, var(--panel-top) 54px, var(--white) 54px);
    box-shadow: 0 0 8px rgba(0,0,0,0.08);
  }

  .top-band {
    position: absolute; left: 0; top: 72px; width: 1200px; height: 84px;
    background: linear-gradient(to bottom, var(--teal-light), var(--teal) 55%, var(--teal-dark));
    box-shadow: 0 3px 5px rgba(0,0,0,0.15);
  }
  .top-band::before, .top-band::after {
    content: ""; position: absolute; left: 0; right: 0;
    border-top: 2px dashed rgba(255,255,255,0.75);
  }
  .top-band::before { top: 5px; }
  .top-band::after { bottom: 5px; }

  .brand {
    position: absolute; left: 180px; top: 16px; width: 192px; height: 192px;
    border-radius: 50%; background: var(--white);
    box-shadow: 0 3px 8px rgba(0,0,0,0.2);
    display: flex; align-items: center; justify-content: center; text-align: center;
  }
  .brand-name {
    font-family: var(--sans); font-weight: 700; font-size: 36px; line-height: 1.05;
    color: var(--teal);
  }

  .phone {
    position: absolute; left: 746px; top: 101px; display: flex; align-items: center; gap: 10px;
    color: var(--white); font-size: 21px;
  }
  .phone svg { width: 24px; height: 28px; }

  .social { position: absolute; top: 96px; display: flex; gap: 15px; left: 944px; }
  .social-link {
    width: 42px; height: 42px; border-radius: 50%;
    background: radial-gradient(circle at 40% 35%, #ffffff, #d9e6e8);
    box-shadow: 0 1px 3px rgba(0,0,0,0.25);
  }

  .side-menu { position: absolute; left: 147px; top: 226px; list-style: none; }
  .side-menu li { margin-bottom: 2px; }
  .side-menu a {
    display: block; width: 228px; height: 51px; padding: 9px 0 0 12px;
    font-family: var(--script); font-weight: 500; font-size: 24px; color: var(--white);
    text-decoration: none;
    background: linear-gradient(to bottom, var(--teal-light), var(--teal-dark));
    clip-path: polygon(0 0, 100% 0, 94% 50%, 100% 100%, 0 100%);
    border-left: 6px solid #1b6b77;
  }
  .side-menu a.is-active { color: var(--gold); }

  .slider {
    position: absolute; left: 390px; top: 230px; width: 652px; height: 308px; overflow: hidden;
  }
  .slide-photo {
    position: absolute; inset: 0;
    background: linear-gradient(110deg, #9fd6df 0%, #c9e9ee 35%, #e8ecec 60%, #b98e5a 100%);
  }
  .slide-caption {
    position: absolute; left: 0; top: 220px; width: 100%; height: 54px;
    background: rgba(255,255,255,0.9); border-bottom: 2px solid #e0ddd4;
    font-size: 20px; color: var(--ink); padding: 16px 0 0 13px;
  }
  .price-badge {
    position: absolute; left: 550px; top: 202px; width: 92px; height: 92px; border-radius: 50%;
    background: radial-gradient(circle at 50% 35%, var(--gold), var(--gold-dark));
    border: 4px solid var(--white); box-shadow: 0 2px 6px rgba(0,0,0,0.25);
    color: var(--white); font-size: 22px; display: flex; align-items: center; justify-content: center;
  }
  .slide-dots { position: absolute; top: 280px; left: 280px; display: flex; gap: 8px; }
  .slide-dots span {
    width: 15px; height: 15px; border-radius: 50%; border: 2px solid var(--white);
    background: rgba(255,255,255,0.3);
  }
  .slide-dots span.is-current { background: #9a9a9a; box-shadow: inset 0 0 0 2px var(--white); }

  .intro { position: absolute; left: 432px; top: 562px; width: 576px; }
  .intro h1 {
    font-family: var(--script); font-weight: 500; font-size: 30px; color: var(--heading);
    text-align: center; margin-left: -30px; margin-bottom: 22px; white-space: nowrap;
  }
  .intro p { font-size: 15px; line-height: 18px; text-align: justify; margin-bottom: 16px; }
</style>
</head>
<body>
  <div class="content-panel"></div>

  <header class="top-band"></header>

  <div class="brand">
    <span class="brand-name">Hazel<br>Bakes</span>
  </div>

  <div class="phone">
    <svg viewBox="0 0 24 28" aria-hidden="true">
      <path fill="#ffffff" d="M6 1c1.5-.5 2.5 0 3 1.5l1.6 4.5c.4 1.2 0 2-1 2.7L8 10.8c.8 3 2.8 6.2 5.3 8.2l1.6-1.2c1-.7 2-.6 2.8.3l3 3.6c.9 1.1.7 2.2-.4 3.1l-1.8 1.4c-1.6 1.2-3.6 1.1-5.6-.3C7 21.7 2.7 14.6 2 8.3 1.8 5.5 3 2.3 6 1z"/>
    </svg>
    <span>+11 40455060</span>
  </div>

  <nav class="social" aria-label="Redes sociales">
    <a class="social-link" href="#" aria-label="Red social 1"></a>
    <a class="social-link" href="#" aria-label="Red social 2"></a>
  </nav>

  <ul class="side-menu">
    <li><a class="is-active" href="#inicio">Inico</a></li>
    <li><a href="#productos">Productos\ Tortas</a></li>
    <li><a href="#contacto">Contacto</a></li>
    <li><a href="#form">Form</a></li>
  </ul>

  <section class="slider">
    <div class="slide-photo" role="img" aria-label="Foto de un cupcake con crema turquesa junto a una tarjeta de la pastelería"></div>
    <div class="slide-caption">Cupcakes’ name</div>
    <div class="price-badge">$19.00</div>
    <div class="slide-dots"><span class="is-current"></span><span></span><span></span></div>
  </section>

  <main class="intro" id="inicio">
    <h1>Los mejores Cupcakes y Pasteles de Santiago!</h1>
    <p>Finalmente ya está disponible en <strong>Santiago de Chile</strong> nuestro catálogo de sabrosos Cupcakes y Tortas.</p>
    <p>Con ingredientes <strong>100% naturales</strong> y elaborados artesanalmente.</p>
    <p>No solo hay que tener en cuenta la presentación fabulosa de los mismos, lo que más destaca es su sabor, que sorprende en cada bocado.</p>
  </main>
</body>
</html>
```